STOREFRONT SIGNAGE/ NEW LOGO

Looking for someone to enhance my current sign idea. I own a pawn shop , which is also a gun shop. I want a catchy front sign, which will be a lighted box sign. I may want to incorporate some symbols or character symbology that highlight firearms, such as : guns, ammo, targets, scope retical , gold, diamonds, cash, watches and/or pawn balls, and im open to other ideas, but i do not want it too busy, i want it simple, with a twist. Attached, you will find a very basic design, showing the business name and the verbiage that I would like to be incorporated into the design. God bless and thank you. may the best design win !

```html
<!DOCTYPE html>
<html lang="en">
<head>
<meta charset="utf-8">
<title>Meridian Gold &amp; Gun Exchange – Storefront Sign</title>
<link href="https://fonts.googleapis.com/css2?family=Archivo+Black&family=Arimo:wght@700&family=Oswald:wght@600&display=swap" rel="stylesheet">
<style>
  :root {
    --backdrop: #1b1715;
    --sign-white: #ffffff;
    --sign-blue: #1f36c8;
    --sign-red: #ec1c24;
    --gold: #b88f0e;
    --guns-yellow: #f6e61c;
    --ink: #111111;
  }
  * { margin: 0; padding: 0; box-sizing: border-box; }
  html, body {
    width: 1200px;
    height: 675px;
    overflow: hidden;
    background: var(--backdrop);
  }
  .canvas {
    position: relative;
    width: 1200px;
    height: 675px;
  }
  .sign {
    position: absolute;
    left: 40px;
    top: 137px;
    width: 1120px;
    height: 400px;
    overflow: hidden;
  }
  .sign-panels {
    position: absolute;
    inset: 0;
    width: 100%;
    height: 100%;
  }
  .headline-small {
    position: absolute;
    left: 38px;
    top: 8px;
    font-family: "Oswald", sans-serif;
    font-weight: 600;
    font-size: 104px;
    line-height: 1;
    color: var(--gold);
    letter-spacing: -1px;
    white-space: nowrap;
    transform: scaleX(0.74);
    transform-origin: left top;
  }
  .headline-large {
    position: absolute;
    left: 28px;
    top: 150px;
    font-family: "Archivo Black", sans-serif;
    font-size: 102px;
    line-height: 1;
    color: var(--gold);
    white-space: nowrap;
    transform: scale(0.92, 1.22);
    transform-origin: left top;
  }
  .cash-line {
    position: absolute;
    left: 95px;
    top: 312px;
    font-family: "Archivo Black", sans-serif;
    font-size: 56px;
    line-height: 1;
    color: var(--sign-white);
    white-space: nowrap;
    transform: scaleY(1.12);
    transform-origin: left top;
  }
  .name-badge {
    position: absolute;
    left: 470px;
    top: 40px;
    width: 210px;
    height: 60px;
    background: var(--gold);
    border: 3px solid var(--ink);
    border-radius: 14px;
    display: flex;
    align-items: center;
    justify-content: center;
    font-family: "Arimo", sans-serif;
    font-weight: 700;
    font-size: 30px;
    color: var(--ink);
    letter-spacing: 1px;
  }
  .services {
    position: absolute;
    list-style: none;
    font-family: "Arimo", sans-serif;
    font-weight: 700;
    font-size: 34px;
    line-height: 46px;
    color: var(--sign-white);
  }
  .services li {
    display: flex;
    align-items: center;
    gap: 14px;
    white-space: nowrap;
  }
  .services li::before {
    content: "";
    width: 16px;
    height: 16px;
    border-radius: 50%;
    background: var(--gold);
    flex: none;
  }
  .services-main { left: 738px; top: 140px; }
  .services-extra { left: 898px; top: 163px; }
  .guns-tag {
    position: absolute;
    left: 830px;
    top: 312px;
    font-family: "Arimo", sans-serif;
    font-weight: 700;
    font-size: 50px;
    line-height: 1;
    color: var(--guns-yellow);
    white-space: nowrap;
  }
</style>
</head>
<body>
<main class="canvas">
  <section class="sign" aria-label="Meridian Gold and Gun Exchange lighted box sign">
    <svg class="sign-panels" viewBox="0 0 1120 400" preserveAspectRatio="none" aria-hidden="true">
      <rect class="panel-white" x="0" y="0" width="1120" height="400" fill="var(--sign-white)"/>
      <rect class="band-red" x="0" y="300" width="820" height="100" fill="var(--sign-red)"/>
      <path class="panel-blue" d="M470 0 C560 110 680 260 780 400 L1120 400 L1120 0 Z" fill="var(--sign-blue)"/>
      <path class="panel-edge" d="M470 0 C560 110 680 260 780 400" fill="none" stroke="var(--ink)" stroke-width="2"/>
    </svg>

    <h1 class="headline-small">GOLD &amp; GUN</h1>
    <p class="headline-large">EXCHANGE</p>
    <p class="cash-line">CASH FOR GOLD</p>

    <div class="name-badge">MERIDIAN</div>

    <ul class="services services-main">
      <li>PAWN</li>
      <li>BUY</li>
      <li>SELL</li>
    </ul>
    <ul class="services services-extra">
      <li>TRADE</li>
      <li>LAYAWAY</li>
    </ul>

    <p class="guns-tag">&amp; GUNS</p>
  </section>
</main>
</body>
</html>
```